Business Card/Stationary
General Contractor
Thank You for all of the submissions so far.
I have eliminated those that had too many curved lines. I like any lines to be more perpendicular/parallel. However, I have left a few with curved lines that I like.
I do like the solid colors on the front and or back.
I have not seen any stationary submissions. I need some of those as well, although not as critical as a business card.
Thank You for your submissions. I will comment again in a couple of days.

```html
<!DOCTYPE html>
<html lang="en">
<head>
<meta charset="utf-8">
<title>Norvale Builders — Business Cards</title>
<link href="https://fonts.googleapis.com/css2?family=Open+Sans:wght@400;600;700&display=swap" rel="stylesheet">
<style>
  :root {
    --canvas: #e9e7e4;
    --white: #ffffff;
    --ink: #3a3a3a;
    --muted: #7a7a7a;
    --accent: #f08a12;
    --accent-deep: #e0560f;
    --accent-light: #f9ad2a;
    --blue-light: #3d93dc;
    --blue-deep: #123f7a;
    --black-light: #4a4a4a;
    --black-deep: #0f0f0f;
    --frame: #dcdcdc;
  }
  * { box-sizing: border-box; margin: 0; padding: 0; }
  html, body { width: 1200px; height: 895px; overflow: hidden; }
  body {
    background: var(--canvas);
    font-family: "Open Sans", Arial, sans-serif;
    position: relative;
  }
  .card {
    position: absolute;
    width: 340px;
    height: 194px;
    border-radius: 3px;
    box-shadow: 0 4px 14px rgba(0,0,0,.18);
    overflow: hidden;
  }
  /* positions */
  .card--orange { left: 50px;  top: 233px; }
  .card--front-a { left: 430px; top: 233px; }
  .card--blue   { left: 810px; top: 233px; }
  .card--black  { left: 240px; top: 467px; }
  .card--front-b { left: 620px; top: 467px; }

  /* backs */
  .card-back { color: var(--white); text-align: center; }
  .card--orange { background: linear-gradient(215deg, var(--accent-light) 0%, var(--accent) 40%, var(--accent-deep) 100%); }
  .card--blue   { background: linear-gradient(215deg, var(--blue-light) 0%, #2467b4 45%, var(--blue-deep) 100%); }
  .card--black  { background: linear-gradient(215deg, var(--black-light) 0%, #222 50%, var(--black-deep) 100%); }

  .brand { display: flex; align-items: center; gap: 6px; font-weight: 700; letter-spacing: .5px; }
  .brand-mark { width: 16px; height: 16px; }
  .card-back .brand { position: absolute; top: 34px; left: 50%; transform: translateX(-50%); font-size: 20px; color: var(--white); }
  .card-back .brand-mark { background: var(--white); }
  .rule { position: absolute; left: 0; right: 0; top: 70px; height: 1px; background: rgba(255,255,255,.55); }
  .services { position: absolute; top: 84px; left: 0; right: 0; list-style: none; font-size: 7.5px; line-height: 11px; }
  .license { position: absolute; left: 14px; bottom: 12px; font-size: 7px; }
  .license-rule { position: absolute; left: 14px; bottom: 26px; width: 70px; height: 1px; background: rgba(255,255,255,.55); }

  /* fronts */
  .card-front { background: var(--white); color: var(--ink); }
  .card-front .brand { position: absolute; top: 22px; left: 16px; font-size: 20px; color: var(--ink); }
  .card-front .brand-mark { background: var(--accent); }
  .name-band {
    position: absolute; right: 0; top: 20px; width: 150px; height: 30px;
    background: var(--accent); color: var(--white);
    font-size: 14px; font-weight: 600; line-height: 30px; padding-left: 12px;
  }
  .frame { position: absolute; right: 14px; top: 60px; width: 136px; height: 70px; border: 1px solid var(--frame); }
  .address { position: absolute; font-size: 7px; line-height: 10px; color: var(--muted); }
  .card--front-a .address { left: 16px; top: 62px; }
  .card--front-b .address { left: 190px; top: 70px; }
  .contacts { position: absolute; left: 16px; bottom: 16px; list-style: none; font-size: 7px; line-height: 10px; color: var(--muted); }
  .contacts span { color: var(--accent); display: inline-block; width: 26px; }
</style>
</head>
<body>

<section class="card card--orange card-back">
  <div class="brand"><span class="brand-mark"></span>norvale</div>
  <div class="rule"></div>
  <ul class="services">
    <li>General Contractor</li>
    <li>Construction Management</li>
    <li>Disaster Response</li>
    <li>Fire/Water/Smoke Damage Restoration</li>
    <li>Mold Assessment/Remediation/Prevention</li>
  </ul>
  <div class="license-rule"></div>
  <div class="license">CGC 1509924</div>
</section>

<section class="card card--front-a card-front">
  <div class="brand"><span class="brand-mark"></span>norvale</div>
  <div class="name-band">Dario M. Venn</div>
  <div class="frame"></div>
  <p class="address">4410 Harbor Lane<br>Suite 200<br>Coral Bay, FL 33401</p>
  <ul class="contacts">
    <li><span>Phone</span>555 210-4400</li>
    <li><span>Cell</span>555 210-4415</li>
    <li><span>Fax</span>555 210-4490</li>
    <li><span>Email</span>dario@norvalebuilders.com</li>
  </ul>
</section>

<section class="card card--blue card-back">
  <div class="brand"><span class="brand-mark"></span>norvale</div>
  <div class="rule"></div>
  <ul class="services">
    <li>General Contractor</li>
    <li>Construction Management</li>
    <li>Disaster Response</li>
    <li>Fire/Water/Smoke Damage Restoration</li>
    <li>Mold Assessment/Remediation/Prevention</li>
  </ul>
  <div class="license-rule"></div>
  <div class="license">CGC 1509924</div>
</section>

<section class="card card--black card-back">
  <div class="brand"><span class="brand-mark"></span>norvale</div>
  <div class="rule"></div>
  <ul class="services">
    <li>General Contractor</li>
    <li>Construction Management</li>
    <li>Disaster Response</li>
    <li>Fire/Water/Smoke Damage Restoration</li>
    <li>Mold Assessment/Remediation/Prevention</li>
  </ul>
  <div class="license-rule"></div>
  <div class="license">CGC 1509924</div>
</section>

<section class="card card--front-b card-front">
  <div class="brand"><span class="brand-mark"></span>norvale</div>
  <div class="name-band">Dario M. Venn</div>
  <p class="address">4410 Harbor Lane<br>Suite 200<br>Coral Bay, FL 33401</p>
  <ul class="contacts">
    <li><span>Phone</span>555 210-4400</li>
    <li><span>Cell</span>555 210-4415</li>
    <li><span>Fax</span>555 210-4490</li>
    <li><span>Email</span>dario@norvalebuilders.com</li>
  </ul>
</section>

</body>
</html>
```